Looking to update current business card

We have a two sided card currently that needs a fresher, newer look. I like the fact it has two sides with a list of products/services we offer on the back side but the overall front look is lackluster. Our logo will stay the same.. I just want someone to bring some new life into the business card.

I like cards that have rounded corners but not sure if there's enough room?

Attached is our current biz card design and logo.

Target Market(s)

business customers

Industry/Entity Type

Business

Contact Information for Business Card

see above

```html
<!DOCTYPE html>
<html lang="en">
<head>
<meta charset="utf-8">
<title>Ridgeline Cyber Group – Business Card</title>
<link href="https://fonts.googleapis.com/css2?family=Open+Sans:wght@400;600;700&family=Exo+2:wght@500&display=swap" rel="stylesheet">
<style>
  :root{
    --backdrop:#e9e6e1;
    --paper:#ffffff;
    --brand-blue:#2f6ea6;
    --brand-blue-dark:#245684;
    --brand-orange:#f0913f;
    --text-grey:#5b5f66;
    --rule:#f3b47a;
  }
  *{box-sizing:border-box;margin:0;padding:0}
  html,body{width:1200px;height:1023px;overflow:hidden}
  body{
    background:var(--backdrop);
    font-family:"Open Sans",Arial,sans-serif;
    display:flex;flex-direction:column;align-items:center;justify-content:center;gap:64px;
  }
  .card{
    width:620px;height:354px;border-radius:6px;position:relative;overflow:hidden;
    box-shadow:0 6px 18px rgba(0,0,0,.18);
  }

  /* Front */
  .card--front{background:var(--paper)}
  .front__rule{position:absolute;left:330px;right:0;top:118px;height:1px;background:var(--rule)}
  .front__brand{
    position:absolute;left:44px;top:84px;
    font-weight:700;font-size:25px;color:var(--brand-blue);letter-spacing:.3px;
  }
  .front__person{position:absolute;left:44px;top:150px}
  .person__name{font-weight:600;font-size:21px;color:var(--brand-blue)}
  .person__title{font-size:14px;color:var(--text-grey);margin-top:4px}
  .front__contacts{position:absolute;left:44px;top:222px;list-style:none}
  .contact{display:flex;align-items:center;gap:10px;font-size:14px;color:var(--text-grey);line-height:23px}
  .contact__icon{width:15px;height:15px;flex:none}
  .front__address{
    position:absolute;left:44px;bottom:28px;
    font-weight:700;font-size:14px;letter-spacing:.6px;color:var(--brand-orange);text-transform:uppercase;
  }

  /* Back */
  .card--back{background:linear-gradient(160deg,#4a8bc4 0%,var(--brand-blue) 45%,var(--brand-blue-dark) 100%)}
  .back__heading{
    position:absolute;left:44px;top:30px;
    font-family:"Exo 2",Arial,sans-serif;font-weight:500;font-size:22px;letter-spacing:2px;
    color:var(--brand-orange);text-transform:uppercase;
  }
  .services{position:absolute;left:44px;top:74px;list-style:none}
  .service{position:relative;padding-left:16px;font-size:13.5px;line-height:20.5px;color:#fff}
  .service::before{
    content:"";position:absolute;left:0;top:7px;width:7px;height:7px;border-radius:50%;background:var(--brand-orange);
  }
  .back__brand{
    position:absolute;right:40px;bottom:40px;
    font-weight:700;font-size:23px;color:#fff;letter-spacing:.3px;
  }
</style>
</head>
<body>

  <section class="card card--front" aria-label="Business card front">
    <div class="front__rule"></div>
    <div class="front__brand">Ridgeline Cyber Group, Inc.</div>
    <div class="front__person">
      <div class="person__name">Daniel Hartwell</div>
      <div class="person__title">Director</div>
    </div>
    <ul class="front__contacts">
      <li class="contact">
        <svg class="contact__icon" viewBox="0 0 16 16" aria-hidden="true">
          <rect width="16" height="16" rx="3" fill="var(--rule)"/>
          <path d="M5 3.5l2 2-1 1.3c.6 1.3 1.6 2.3 2.9 2.9l1.3-1 2 2-1.2 1.6C7.6 12 4 8.4 3.7 4.6z" fill="#fff"/>
        </svg>
        555.210.4800
      </li>
      <li class="contact">
        <svg class="contact__icon" viewBox="0 0 16 16" aria-hidden="true">
          <rect width="16" height="16" rx="3" fill="var(--rule)"/>
          <rect x="4" y="6" width="8" height="5" rx="1" fill="#fff"/>
          <rect x="5.5" y="3.5" width="5" height="2.5" fill="#fff"/>
        </svg>
        800.555.0142
      </li>
      <li class="contact">
        <svg class="contact__icon" viewBox="0 0 16 16" aria-hidden="true">
          <rect width="16" height="16" rx="3" fill="var(--rule)"/>
          <rect x="3.5" y="5" width="9" height="6.5" fill="#fff"/>
          <path d="M3.5 5l4.5 3.5L12.5 5" fill="none" stroke="var(--rule)" stroke-width="1"/>
        </svg>
        dhartwell@ridgelinecg.com
      </li>
    </ul>
    <div class="front__address">18 Harbor Lane, Fairview, MA 02100</div>
  </section>

  <section class="card card--back" aria-label="Business card back">
    <h2 class="back__heading">Security Solutions and Services</h2>
    <ul class="services">
      <li class="service">Anti-Virus / Malware</li>
      <li class="service">Anti-Spam</li>
      <li class="service">Backup / Disaster Recovery</li>
      <li class="service">Email Archiving</li>
      <li class="service">Encryption</li>
      <li class="service">Firewall</li>
      <li class="service">Mobile Security / BYOD</li>
      <li class="service">Network Access Control (NAC)</li>
      <li class="service">Patch Management</li>
      <li class="service">Penetration Testing and Security Assessments</li>
      <li class="service">Virtualization</li>
      <li class="service">Web Filtering</li>
    </ul>
    <div class="back__brand">Ridgeline Cyber Group, Inc.</div>
  </section>

</body>
</html>
```